Lantern over The Moor Business Card Design

Simple 2 sided card ideally based around a zen garden approach (larger stone in a sand combed garden), but not essential.
Business is Project Management, IT Consultancy, Business Analysis.
Initially one person, however others may join the business so a unique logo would be preferred that encapsulates the approach of one pebble dropping in water causing many ripples. Potentially based around a zen garden, but not essential.
Clean and tidy, double sided, glossy, interesting and unique.
Company Name and contact details on one side (with the ability to replace the name, telephone and email address for more staff):
Lantern over The Moor Ltd
Derek Holbrook
077 5182 6207
derek@lanternoverthemoor.example
Company name and offering on the other:
Lantern over The Moor Ltd
Project Management
Business Analysis
IT Consultancy
Interesting looking font, nice colours, not too many, but simple, effective and eye catching.
Potential Image either as a background or to the left/ right. Replicated on the rear of the card.
Design once approved and complete to be the sole property of Lantern over The Moor Ltd.
No requirement for Twitter, Facebook or Linked in details on any design
Lantern over The Moor
Derek Holbrook
077 5182 6207
Project Management
Business Analysis
IT Consultancy

```html
<!DOCTYPE html>
<html lang="en">
<head>
<meta charset="utf-8">
<title>Lantern over The Moor Business Card Design</title>
<link rel="stylesheet" href="https://fonts.googleapis.com/css2?family=Roboto+Condensed:wght@700&family=Open+Sans:wght@600;700&family=Arimo&display=swap">
<style>
  :root {
    --bg: #e9e7e4;
    --card: #ffffff;
    --red: #d4202a;
    --blue: #114e98;
    --yellow: #f0e816;
    --name-blue: #1b56a1;
    --ink: #111111;
    --star: #1f3f8f;
    --art-light: #f4f4f4;
    --art-mid: #dcdcdc;
  }
  html, body {
    margin: 0;
    padding: 0;
    width: 1200px;
    height: 1200px;
    overflow: hidden;
    background: var(--bg);
  }
  .canvas {
    position: relative;
    width: 1200px;
    height: 1200px;
  }
  .card {
    position: absolute;
    left: 175px;
    width: 850px;
    height: 560px;
    background: var(--card);
    overflow: hidden;
    box-shadow: 0 2px 6px rgba(0,0,0,0.18);
  }
  .card--front { top: 30px; }
  .card--back { top: 610px; }
  .card__bands {
    position: absolute;
    inset: 0;
    width: 850px;
    height: 560px;
  }
  .card__company {
    position: absolute;
    left: 34px;
    right: 34px;
    top: 70px;
    margin: 0;
    font-family: "Roboto Condensed", "Arial Narrow", sans-serif;
    font-weight: 700;
    font-size: 69px;
    line-height: 1;
    color: #ffffff;
    text-transform: uppercase;
    white-space: nowrap;
    letter-spacing: 0;
  }
  .person {
    position: absolute;
    left: 52px;
    top: 350px;
    font-family: "Open Sans", Arial, sans-serif;
  }
  .person__name {
    margin: 0 0 22px;
    font-size: 36px;
    font-weight: 700;
    color: var(--name-blue);
    line-height: 1.1;
  }
  .contact {
    list-style: none;
    margin: 0;
    padding: 0;
  }
  .contact__item {
    display: flex;
    align-items: center;
    gap: 22px;
    height: 46px;
    font-size: 28px;
    font-weight: 600;
    color: var(--ink);
  }
  .contact__icon {
    width: 34px;
    height: 30px;
    flex: none;
  }
  .services {
    position: absolute;
    left: 42px;
    top: 294px;
    list-style: none;
    margin: 0;
    padding: 0;
    font-family: "Arimo", Arial, sans-serif;
    font-size: 34px;
    color: var(--ink);
  }
  .services__item {
    display: flex;
    align-items: center;
    gap: 18px;
    height: 54px;
  }
  .services__star {
    width: 32px;
    height: 32px;
    flex: none;
  }
  .process-art {
    position: absolute;
    left: 452px;
    top: 320px;
    width: 330px;
    height: 240px;
    background: linear-gradient(160deg, var(--art-light), var(--art-mid));
  }
</style>
</head>
<body>
<div class="canvas">

  <section class="card card--front" aria-label="Business card front">
    <svg class="card__bands" viewBox="0 0 850 560" aria-hidden="true">
      <polygon fill="var(--blue)" points="0,0 529,0 850,126 850,334 457,190 0,190"/>
      <polygon fill="var(--red)" points="0,22 457,190 0,190"/>
      <polygon fill="var(--yellow)" points="529,0 850,0 850,126"/>
    </svg>
    <h1 class="card__company">Lantern over The Moor</h1>
    <div class="person">
      <h2 class="person__name">Derek Holbrook</h2>
      <ul class="contact">
        <li class="contact__item">
          <svg class="contact__icon" viewBox="0 0 34 30" aria-hidden="true">
            <path fill="var(--ink)" d="M3 9c0-4 6-6 14-6s14 2 14 6v3h-7V9c-2-1-5-1-7-1s-5 0-7 1v3H3z"/>
            <path fill="var(--ink)" d="M9 12h16l5 9v7H4v-7z"/>
            <circle cx="17" cy="20" r="4.5" fill="#fff"/>
            <circle cx="17" cy="20" r="2" fill="var(--ink)"/>
          </svg>
          <span>077 5182 6207</span>
        </li>
        <li class="contact__item">
          <svg class="contact__icon" viewBox="0 0 34 30" aria-hidden="true">
            <rect x="2" y="5" width="30" height="20" rx="1.5" fill="var(--ink)"/>
            <polyline points="4,8 17,18 30,8" fill="none" stroke="#fff" stroke-width="2"/>
            <line x1="4" y1="23" x2="13" y2="15" stroke="#fff" stroke-width="2"/>
            <line x1="30" y1="23" x2="21" y2="15" stroke="#fff" stroke-width="2"/>
          </svg>
          <span>derek@lanternoverthemoor.example</span>
        </li>
      </ul>
    </div>
  </section>

  <section class="card card--back" aria-label="Business card back">
    <svg class="card__bands" viewBox="0 0 850 560" aria-hidden="true">
      <polygon fill="var(--blue)" points="0,0 529,0 850,126 850,334 457,190 0,190"/>
      <polygon fill="var(--red)" points="0,22 457,190 0,190"/>
      <polygon fill="var(--yellow)" points="529,0 850,0 850,126"/>
    </svg>
    <h1 class="card__company">Lantern over The Moor</h1>
    <ul class="services">
      <li class="services__item">
        <svg class="services__star" viewBox="0 0 24 24" aria-hidden="true"><polygon fill="var(--star)" points="12,1 15,9 23,9 16.5,14 19,22 12,17 5,22 7.5,14 1,9 9,9"/></svg>
        <span>Project Management</span>
      </li>
      <li class="services__item">
        <svg class="services__star" viewBox="0 0 24 24" aria-hidden="true"><polygon fill="var(--star)" points="12,1 15,9 23,9 16.5,14 19,22 12,17 5,22 7.5,14 1,9 9,9"/></svg>
        <span>Business Analysis</span>
      </li>
      <li class="services__item">
        <svg class="services__star" viewBox="0 0 24 24" aria-hidden="true"><polygon fill="var(--star)" points="12,1 15,9 23,9 16.5,14 19,22 12,17 5,22 7.5,14 1,9 9,9"/></svg>
        <span>IT Consultancy</span>
      </li>
    </ul>
    <div class="process-art" role="img" aria-label="Photo of a hand sketching a process flowchart with a marker"></div>
  </section>

</div>
</body>
</html>
```